New counselling and hypnotherapy business

I'd like a flyer which is relevant to people who want support and to improve their wellbeing which follows the same theme as my website: http://larkmoretherapy.plumweave.com
And emphasise that whatever the area of concern, development or growth and I can tailor my knowledge and skills to help.

I'd like to use the same logo and my emphasis is to draw the audience in...therapy and counselling is for people who are "stuck" and having a difficult time...it can also be useful has a personal development tool.

Hypnotherapy

```html
<!DOCTYPE html>
<html lang="en">
<head>
<meta charset="utf-8">
<title>Larkmore Counselling &amp; Hypnotherapy — Flyer</title>
<link href="https://fonts.googleapis.com/css2?family=Bebas+Neue&display=swap" rel="stylesheet">
<style>
  :root{
    --purple-deep:#6d3379;
    --purple:#7d4689;
    --purple-soft:#a58bab;
    --purple-mist:#e9deec;
    --paper:#ffffff;
    --rule:#b9a3bf;
    --photo-warm:#e9c3a6;
    --photo-light:#f6ede6;
  }
  *{margin:0;padding:0;box-sizing:border-box}
  html,body{width:933px;height:1200px;overflow:hidden;background:#fff}
  .flyer{
    position:relative;width:933px;height:1200px;overflow:hidden;
    font-family:"Bebas Neue",sans-serif;color:var(--purple);
    background:radial-gradient(ellipse at 75% 35%, #ffffff 0%, #f6f1f7 55%, #e8dcec 100%);
  }
  .headline{position:absolute;left:20px;top:14px;width:900px;line-height:1.07;font-size:75px;letter-spacing:-1px;word-spacing:-4px}
  .headline .soft{color:var(--purple-soft)}
  .headline .strong{color:var(--purple-deep)}
  .headline-rule{position:absolute;left:14px;top:186px;width:905px;height:3px;background:var(--rule)}
  .intro{position:absolute;left:18px;top:200px;width:900px;font-size:21.5px;line-height:27px;color:var(--purple-soft);letter-spacing:0.1px}
  .intro p+p{margin-top:27px}
  .services{position:absolute;left:20px;top:461px;width:440px;list-style:none;font-size:21.5px;line-height:27px;color:var(--purple-deep)}
  .services li{position:relative;padding-left:26px;margin-bottom:27px}
  .services li::before{content:"";position:absolute;left:0;top:8px;width:11px;height:11px;border-radius:50%;background:var(--purple-soft)}
  .photo{
    position:absolute;left:420px;top:420px;width:513px;height:500px;
    background:radial-gradient(ellipse at 55% 40%, var(--photo-warm) 0%, #f0d8c6 40%, rgba(246,237,230,0) 75%);
  }
  .swoosh{position:absolute;left:0;top:0}
  .brand{position:absolute;left:30px;top:1030px;width:260px;display:flex;align-items:center;gap:12px}
  .brand-dot{width:22px;height:22px;border-radius:50%;background:var(--purple);flex:none}
  .brand-name{font-size:30px;line-height:30px;color:var(--purple)}
  .contact{position:absolute;right:20px;top:950px;text-align:right;color:#fff}
  .contact-lead{font-size:24px;letter-spacing:0.3px}
  .contact-phone{display:flex;align-items:center;justify-content:flex-end;gap:12px;font-size:76px;line-height:78px;margin-top:4px}
  .contact-line{font-size:30px;line-height:34px}
  .address-band{position:absolute;left:0;top:1148px;width:933px;height:52px;background:var(--purple);color:#fff;font-size:24px;line-height:52px;padding-left:16px;letter-spacing:0.2px}
</style>
</head>
<body>
<main class="flyer">
  <h1 class="headline">
    <span class="soft">Would</span> <span class="strong">you</span> <span class="soft">like</span> <span class="strong">a new beginning?</span><br>
    <span class="soft">To</span> <span class="strong">talk?</span> <span class="soft">To</span> <span class="strong">be heard?</span> <span class="soft">To</span> <span class="strong">be you?</span>
  </h1>
  <div class="headline-rule"></div>

  <section class="intro">
    <p>There are times in all of our lives when we feel we have lost our way, we need a listening ear or we simply want somebody to work together with to help us reach the next step in our journey, whatever that may be. Maybe that sounds like you and you're looking for somebody to help you take that first step or maybe you simply want somebody to share your concerns with and really feel heard.</p>
    <p>I am a fully qualified counsellor and I'm able to provide a safe, confidential environment for you to speak, to feel, to be heard and valued as an individual in what can be a scary and challenging world.</p>
  </section>

  <div class="photo" role="img" aria-label="Photograph of a smiling, laughing couple embracing in bright sunlight"></div>

  <ul class="services">
    <li>Experience working with people with a wide range of concerns – loss &amp; grief, depression, anxiety, confidence, self-esteem, eating disorders, general personal deployment and growth.</li>
    <li>Wide range of techniques used - tailored to you.</li>
    <li>Supporting individuals over 14 including couples &amp; groups.</li>
    <li>Short, medium and long term therapy.</li>
    <li>Hypnotherapy also available!</li>
  </ul>

  <svg class="swoosh" width="933" height="1200" viewBox="0 0 933 1200" aria-hidden="true">
    <defs>
      <linearGradient id="swooshFill" x1="0" y1="0" x2="1" y2="0">
        <stop offset="0" stop-color="#e6d7ea"/>
        <stop offset="0.45" stop-color="#a77bb1"/>
        <stop offset="1" stop-color="#7d4689"/>
      </linearGradient>
    </defs>
    <path d="M0 940 C250 990 620 930 933 780 L933 1148 L0 1148 Z" fill="url(#swooshFill)"/>
    <path d="M0 905 C300 985 640 930 933 800" fill="none" stroke="#d9c6de" stroke-width="2" opacity="0.8"/>
    <path d="M0 990 C300 1040 650 990 933 880" fill="none" stroke="#fff" stroke-width="1.5" opacity="0.35"/>
    <path d="M0 1040 C320 1080 660 1040 933 950" fill="none" stroke="#fff" stroke-width="1.5" opacity="0.3"/>
    <path d="M0 1090 C340 1120 680 1090 933 1030" fill="none" stroke="#fff" stroke-width="1.5" opacity="0.25"/>
  </svg>

  <div class="brand">
    <span class="brand-dot"></span>
    <span class="brand-name">Larkmore Counselling &amp; Hypnotherapy</span>
  </div>

  <section class="contact">
    <p class="contact-lead">For more information, contact me on...</p>
    <p class="contact-phone">
      <svg width="60" height="60" viewBox="0 0 60 60" aria-hidden="true">
        <circle cx="30" cy="30" r="27" fill="none" stroke="#fff" stroke-width="4"/>
        <path d="M22 15c2 0 5 6 5 8s-3 3-3 5 5 9 8 10c2 0 3-3 5-3s7 3 7 5-4 6-7 6c-9 0-20-14-20-23 0-4 3-8 5-8z" fill="none" stroke="#fff" stroke-width="3" stroke-linejoin="round"/>
      </svg>
      <span>07700 900418</span>
    </p>
    <p class="contact-line">Email: larkmoretherapy@plumweave.com</p>
    <p class="contact-line">www.larkmoretherapy.plumweave.com</p>
  </section>

  <footer class="address-band">Larkmore Counselling &amp; Hypnotherapy, 12B, Harbour Lane, Larkmore, East Sussex BN9 4QT</footer>
</main>
</body>
</html>
```